New Business Card Design Project for Handyman Business

I would like to purchase a customized version of a design you have previously submitted - https://www.plimvaro.example/work/58302716
I love this design!
I am hoping you can design something similar to this for our Handyman Business.
Attached is our logo and some graphics we have used.
Here is a link to the Google Doc with the content that needs to be included, https://files.trenowick.example/sheet/q/4XRKW-7hLp2DnQv8sTc5ma-ZzoeB3kWu9YyTgp6HJ__RmwNdVcQeLbs4jfnv0ztqxhaK7M41p9ggWHe/view
Target Market(s)
Real Estate Agents, Home Owners and Property Managers
Industry/Entity Type
Construction/ Speciality Trade
Contact Information for Business Card
https://files.trenowick.example/sheet/7QpaRzN_ukoyb4cXTwLHhJe8KnuSbPjCr2QDaLy6nwod/view?mode=shared
Font styles to use
Other font styles liked:
- Ubuntu
Look and feel
Each slider illustrates characteristics of the customer's brand and the style your logo design should communicate.

```html
<!DOCTYPE html>
<html lang="en">
<head>
<meta charset="utf-8">
<title>Fixwright Business Card</title>
<link href="https://fonts.googleapis.com/css2?family=Ubuntu:wght@400;500;700&display=swap" rel="stylesheet">
<style>
  :root {
    --stage: #232323;
    --card: #1f2023;
    --card-raised: #27282c;
    --card-mid: #232428;
    --pattern: #2b2c30;
    --blue: #1f78c1;
    --green: #4cb748;
    --muted: #a9abb0;
    --white: #f2f2f2;
  }
  * { box-sizing: border-box; margin: 0; padding: 0; }
  html, body { width: 1200px; height: 780px; overflow: hidden; }
  body {
    background: var(--stage);
    font-family: "Ubuntu", sans-serif;
    color: var(--white);
    position: relative;
  }
  .card {
    position: absolute;
    top: 110px;
    width: 320px;
    height: 560px;
    background: var(--card);
    box-shadow: 0 14px 30px rgba(0,0,0,.55);
    overflow: hidden;
  }
  .card-back { left: 220px; }
  .card-front { left: 660px; }

  /* shared brand name: one colour, one weight, one plain circle */
  .brand { display: flex; align-items: center; gap: 10px; }
  .brand-dot { border-radius: 50%; background: var(--green); flex: none; }
  .brand-name { font-weight: 500; color: var(--white); }

  /* back */
  .back-pattern {
    position: absolute; inset: 0;
    background: linear-gradient(135deg, var(--pattern), #222327 60%, var(--pattern));
  }
  .back-brand { position: absolute; top: 38px; right: 30px; gap: 8px; }
  .back-brand .brand-dot { width: 10px; height: 10px; }
  .back-brand .brand-name { font-size: 22px; }

  /* front */
  .front-layers { position: absolute; inset: 0; }
  .front-content {
    position: absolute; top: 0; left: 0; right: 0;
    display: flex; flex-direction: column; align-items: center;
    text-align: center;
  }
  .front-brand { margin-top: 58px; }
  .front-brand .brand-dot { width: 16px; height: 16px; }
  .front-brand .brand-name { font-size: 36px; letter-spacing: .5px; }
  .brand-tagline {
    margin-top: 8px; font-size: 11px; font-weight: 400;
    letter-spacing: 1.5px; color: var(--muted);
  }
  .person-name { margin-top: 28px; font-size: 28px; font-weight: 700; line-height: 1.1; }
  .person-name .first { color: var(--blue); }
  .person-name .last { color: var(--green); }
  .person-title { margin-top: 4px; font-size: 14px; }
  .icon-row { display: flex; gap: 8px; margin-top: 12px; }
  .icon-dot {
    width: 22px; height: 22px; border-radius: 50%;
    background: var(--green); display: flex; align-items: center; justify-content: center;
  }
  .icon-dot svg { width: 12px; height: 12px; }
  .contact-list { list-style: none; margin-top: 12px; font-size: 13px; line-height: 1.5; }
  .social-row { margin-top: 14px; }
  .social-row .icon-dot { width: 20px; height: 20px; }
  .social-handle { margin-top: 8px; font-size: 12.5px; }

  .services {
    position: absolute; left: 0; right: 0; bottom: 34px;
    text-align: center; font-size: 13px; line-height: 1.5;
  }
  .services .sep {
    display: inline-block; width: 8px; height: 8px; border-radius: 50%;
    background: var(--green); margin: 0 4px; vertical-align: 1px;
  }
</style>
</head>
<body>

<section class="card card-back" aria-label="Card back">
  <div class="back-pattern" role="img" aria-label="Embossed repeating pattern in dark grey"></div>
  <div class="brand back-brand">
    <span class="brand-dot"></span>
    <span class="brand-name">Fixwright</span>
  </div>
</section>

<section class="card card-front" aria-label="Card front">
  <svg class="front-layers" viewBox="0 0 320 560" preserveAspectRatio="none" aria-hidden="true">
    <path d="M0 0 H320 V440 Q150 500 0 480 Z" fill="var(--card-mid)" style="filter:drop-shadow(0 4px 6px rgba(0,0,0,.5))"/>
    <path d="M0 0 H320 V380 Q220 470 0 420 Z" fill="var(--card-raised)" style="filter:drop-shadow(0 5px 8px rgba(0,0,0,.55))"/>
  </svg>

  <div class="front-content">
    <div class="brand front-brand">
      <span class="brand-dot"></span>
      <span class="brand-name">Fixwright</span>
    </div>
    <p class="brand-tagline">Home Care Specialists</p>

    <h1 class="person-name"><span class="first">Dana</span> <span class="last">Whitlock</span></h1>
    <p class="person-title">Owner/ Handyman</p>

    <div class="icon-row">
      <span class="icon-dot"><svg viewBox="0 0 12 12"><path d="M3 1 L5 3 L4 4.5 Q5 7 7.5 8 L9 7 L11 9 L9.5 11 Q2 9.5 1 2.5 Z" fill="#fff"/></svg></span>
      <span class="icon-dot"><svg viewBox="0 0 12 12"><rect x="1" y="3" width="10" height="7" fill="none" stroke="#fff" stroke-width="1.3"/><path d="M1 3 L6 7 L11 3" fill="none" stroke="#fff" stroke-width="1.3"/></svg></span>
      <span class="icon-dot"><svg viewBox="0 0 12 12"><circle cx="6" cy="6" r="4.6" fill="none" stroke="#fff" stroke-width="1.2"/><ellipse cx="6" cy="6" rx="2" ry="4.6" fill="none" stroke="#fff" stroke-width="1"/><path d="M1.4 6 H10.6" stroke="#fff" stroke-width="1"/></svg></span>
    </div>

    <ul class="contact-list">
      <li>(555) 014-2287</li>
      <li>www.fixwright-home.example</li>
      <li>dana@fixwright-home.example</li>
    </ul>

    <div class="icon-row social-row" aria-label="Social profiles">
      <span class="icon-dot"></span>
      <span class="icon-dot"></span>
      <span class="icon-dot"></span>
      <span class="icon-dot"></span>
    </div>
    <p class="social-handle">FixwrightHomeServices</p>
  </div>

  <div class="services">
    <p>Commercial and Residential Handyman</p>
    <p>Improve<span class="sep"></span>Repair<span class="sep"></span>Remodel<span class="sep"></span>Maintain</p>
  </div>
</section>

</body>
</html>
```